Business Card Design Project

I need a business card for an environmentally friendly interior design company called Maplecrest Decor.
I was thinking it might be nice to print the business cards on brown recycled paper with green ink.
In addition to interior design, I will also be able to consult with homeowners regarding their indoor environments and how they might be affecting their health after May 2013 which is when I will complete my certification program. This can be added to the business card at that time: "Certified Dwelling Vitality Environmental Consultant".

```html
<!DOCTYPE html>
<html lang="en">
<head>
<meta charset="utf-8">
<title>Maplecrest Decor – Business Card</title>
<link rel="stylesheet" href="https://fonts.googleapis.com/css2?family=Cabin:wght@400;500;700&family=Nothing+You+Could+Do&display=swap">
<style>
  :root {
    --maroon: #7e2823;
    --leaf: #4f7b14;
    --paper: #ffffff;
  }
  * { margin: 0; padding: 0; box-sizing: border-box; }
  html, body {
    width: 1200px;
    height: 720px;
    overflow: hidden;
    background: var(--paper);
  }
  .card {
    position: relative;
    width: 1200px;
    height: 720px;
    background: var(--paper);
    font-family: "Cabin", sans-serif;
  }
  .brand {
    position: absolute;
    top: 150px;
    left: 0;
    width: 1200px;
    display: flex;
    align-items: center;
    justify-content: center;
    gap: 28px;
  }
  .brand-dot {
    width: 84px;
    height: 84px;
    border-radius: 50%;
    background: var(--leaf);
    flex: none;
  }
  .brand-name {
    font-family: "Cabin", sans-serif;
    font-weight: 400;
    font-size: 118px;
    line-height: 1;
    color: var(--maroon);
    letter-spacing: 1px;
  }
  .tagline {
    position: absolute;
    top: 318px;
    right: 100px;
    font-family: "Nothing You Could Do", cursive;
    font-size: 46px;
    color: var(--maroon);
    line-height: 1;
  }
  .contact {
    position: absolute;
    top: 452px;
    left: 0;
    width: 1200px;
    text-align: center;
  }
  .person-name {
    font-weight: 700;
    font-size: 66px;
    line-height: 1;
    color: var(--maroon);
    margin-bottom: 18px;
  }
  .credential, .details {
    font-weight: 400;
    font-size: 35px;
    line-height: 1.45;
    color: var(--leaf);
  }
  .details .sep { margin: 0 14px; }
</style>
</head>
<body>
  <main class="card">
    <header class="brand">
      <span class="brand-dot" aria-hidden="true"></span>
      <span class="brand-name">Maplecrest Decor</span>
    </header>
    <p class="tagline">environmentally friendly design</p>
    <section class="contact">
      <h1 class="person-name">Clara Jo Bennett</h1>
      <p class="credential">Certified Dwelling Vitality Environmental Consultant</p>
      <p class="details">(713) 555-0148<span class="sep">•</span>hello@maplecrestdecor.com</p>
    </section>
  </main>
</body>
</html>
```